UK garage/funky house night flier

I need a flier design to upload to my sociallink event page and also some printed fliers to promote the event.

Event is in an urban area underneath railway arches so would like a flier to reflect this with an urban background.

new photos uploaded to be used as possible backgrounds

Target Market(s)

aged 18-30

Industry/Entity Type

House

Requirements
Must have
• The following text on front of flier:

TRUE PULSE ENTERTAINMENTS PRESENTS A NIGHT CALLED…

‘MIDNIGHT CELLAR RHYTHMZ’

Saturday 7th September 2013

@ Dock47, Harlow Lane, Digbeth, Birmingham B9 3QW

9pm till late

DJ’s playing a selection of Funky house/deep house/future garage and old school 2-step garage

(On back of flier......)

Come and enjoy yourself in a friendly, safe environment with like-minded people who are out to have a good time and rave till the early hours. This venue is part outdoor terrace and part indoor with music being played on the Wavecraft Soundsystem – so you know it is a night not to be missed!!

This event is guestlist only. Those not on the guest list will not be allowed entry. To get yourself on the guest list go to the sociallink page www.sociallink.example/truepulseentertainments and join the event ‘Midnight Cellar Rhythmz’

Dresscode: smart. No trainers/tracksuits
Admission fee on the door is £5
Last entry: midnight
Nice to have
• must be portrait, A5 or A6 size

Urban background, maybe at night, a street with old brickwork, maybe some speakers in the foreground.

dock47 logo bottom right

Back of flier to have the map of Dock47

```html
<!DOCTYPE html>
<html lang="en">
<head>
<meta charset="utf-8">
<title>Midnight Cellar Rhythmz – Flier</title>
<link href="https://fonts.googleapis.com/css2?family=Arimo:wght@400;700&family=Oswald:wght@500&family=Roboto+Slab:wght@700;900&family=Yesteryear&display=swap" rel="stylesheet">
<style>
  :root {
    --page: #ffffff;
    --ink: #ffffff;
    --night: #0b0810;
    --violet: #7a3fa6;
    --violet-deep: #2a1438;
    --amber: #c98a5a;
    --rule: rgba(255,255,255,0.75);
    --body: #e9e4ee;
  }
  * { box-sizing: border-box; margin: 0; padding: 0; }
  html, body { width: 1200px; height: 848px; overflow: hidden; background: var(--page); }
  .canvas { position: relative; width: 1200px; height: 848px; }

  .flier { position: absolute; top: 48px; height: 748px; background: var(--night); overflow: hidden; color: var(--ink); }
  .flier--front { left: 56px; width: 526px; }
  .flier--back { left: 625px; width: 529px; }

  .photo { position: absolute; left: 0; top: 0; width: 100%; }
  .flier--front .photo {
    height: 100%;
    background:
      radial-gradient(ellipse 45% 25% at 40% 22%, rgba(201,138,90,0.75), transparent 70%),
      radial-gradient(ellipse 60% 45% at 55% 40%, rgba(170,110,210,0.8), transparent 75%),
      linear-gradient(180deg, #3a2a3c 0%, #6b3f8f 35%, #3b2350 55%, #120b18 75%, var(--night) 100%);
  }
  .flier--back .photo {
    height: 230px;
    background:
      radial-gradient(ellipse 30% 35% at 30% 50%, rgba(255,220,170,0.8), transparent 70%),
      radial-gradient(ellipse 70% 60% at 55% 20%, rgba(201,138,90,0.6), transparent 75%),
      linear-gradient(180deg, #5a3a6e 0%, #7a3fa6 45%, rgba(11,8,16,0) 100%);
  }

  .presenter {
    position: absolute; right: 10px; top: 10px;
    writing-mode: vertical-rl;
    font: 500 13px/1 "Oswald", sans-serif; letter-spacing: 1.6px;
  }
  .venue-mark {
    position: absolute; right: 44px; top: 62px;
    display: flex; align-items: center; gap: 8px;
    font: 700 20px/1 "Roboto Slab", serif; letter-spacing: 3px; color: #cfc6d8;
  }
  .venue-mark .dot { width: 12px; height: 12px; border: 2px solid currentColor; }

  .title { position: absolute; text-align: right; white-space: nowrap; }
  .title .script { display: block; font: 400 60px/1 "Yesteryear", cursive; }
  .title .mid { display: block; font: 700 42px/1 "Roboto Slab", serif; letter-spacing: 6px; }
  .title .big { display: block; font: 900 66px/1 "Roboto Slab", serif; letter-spacing: 9px; margin-top: 2px; }

  .flier--front .title { right: 36px; top: 400px; }
  .front-info { position: absolute; right: 36px; top: 616px; text-align: right; }
  .date { font: 500 26px/1 "Oswald", sans-serif; letter-spacing: 0.5px; white-space: nowrap; }
  .address { font: 500 15px/1 "Oswald", sans-serif; letter-spacing: 2px; margin-top: 10px; white-space: nowrap; }
  .lineup { font: 500 14.5px/1.25 "Oswald", sans-serif; letter-spacing: 0.6px; margin-top: 14px; white-space: nowrap; }

  .flier--back .title { right: 36px; top: 32px; }
  .flier--back .title .script { font-size: 50px; }
  .flier--back .title .mid { font-size: 34px; }
  .flier--back .title .big { font-size: 54px; }
  .rule { position: absolute; left: 36px; right: 36px; height: 1px; background: var(--rule); }
  .back-head { position: absolute; left: 36px; top: 202px; }
  .back-head .address { margin-top: 7px; font-size: 14px; letter-spacing: 1.8px; }
  .details { position: absolute; left: 36px; right: 36px; top: 274px; font: 400 13.6px/1.22 "Arimo", sans-serif; color: var(--body); }
  .details p + p { margin-top: 14px; }
  .details strong { color: var(--ink); }

  .map { position: absolute; left: 83px; top: 486px; width: 372px; height: 210px; border-radius: 6px;
    background: linear-gradient(160deg, #2a2235, #1b1524 60%, #241c30); }
  .map-mark { position: absolute; left: 290px; top: 512px; display: flex; align-items: center; gap: 8px;
    font: 700 22px/1 "Roboto Slab", serif; letter-spacing: 3px; }
  .map-mark .dot { width: 14px; height: 14px; border: 2px solid currentColor; }

  .footer { position: absolute; left: 0; right: 0; top: 704px; text-align: center; font: 400 12.5px/1.35 "Arimo", sans-serif; }
  .footer .social { display: inline-flex; align-items: center; gap: 6px; }
  .footer .sq { width: 11px; height: 11px; background: var(--ink); display: inline-block; }
</style>
</head>
<body>
<main class="canvas">

  <section class="flier flier--front">
    <div class="photo" role="img" aria-label="Night photo of a brick railway arch tunnel with graffiti, lit in purple and amber"></div>
    <div class="presenter">TRUE PULSE ENTERTAINMENTS PRESENTS</div>
    <div class="venue-mark"><span class="dot"></span>DOCK47</div>
    <h1 class="title">
      <span class="script">Midnight</span>
      <span class="mid">CELLAR</span>
      <span class="big">RHYTHMZ</span>
    </h1>
    <div class="front-info">
      <p class="date">SATURDAY 7TH SEPTEMBER 2013</p>
      <p class="address">@ DOCK47, HARLOW LANE, DIGBETH, BIRMINGHAM B9 3QW</p>
      <p class="lineup">DJs PLAYING A SELECTION OF FUNKY HOUSE/DEEP HOUSE/FUTURE GARAGE<br>AND OLD SCHOOL 2-STEP GARAGE &nbsp;/&nbsp; 9PM TIL LATE</p>
    </div>
  </section>

  <section class="flier flier--back">
    <div class="photo" role="img" aria-label="Brick railway arches at night with a bright street light"></div>
    <h2 class="title">
      <span class="script">Midnight</span>
      <span class="mid">CELLAR</span>
      <span class="big">RHYTHMZ</span>
    </h2>
    <div class="rule" style="top:190px"></div>
    <div class="back-head">
      <p class="date">SATURDAY 7TH SEPTEMBER 2013</p>
      <p class="address">@ DOCK47, HARLOW LANE, DIGBETH, BIRMINGHAM B9 3QW</p>
    </div>
    <div class="rule" style="top:260px"></div>
    <div class="details">
      <p>Come and enjoy yourself in a friendly, safe environment with like-minded people who are out to have a good time and rave till the early hours. This venue is part outdoor terrace and part indoor with music being played on the <strong>Wavecraft</strong> Soundsystem – so you know it is a night not to be missed!!</p>
      <p><strong>This event is guestlist only.</strong> Those not on the guest list will not be allowed entry.</p>
      <p>To get yourself on the guest list go to the sociallink page <strong>www.sociallink.example/truepulseentertainments</strong> and join the event ‘Midnight Cellar Rhythmz’</p>
    </div>
    <div class="rule" style="top:472px"></div>
    <div class="map" role="img" aria-label="Street map of Digbeth showing the route to Dock47"></div>
    <div class="map-mark"><span class="dot"></span>DOCK47</div>
    <div class="footer">
      <p><strong>£5 ENTRY</strong> / No tracksuits/trainers / Security tight but polite.</p>
      <p>For more information, find us: &nbsp;<span class="social"><span class="sq"></span>truepulseentertainments</span></p>
    </div>
  </section>

</main>
</body>
</html>
```